Natural Skincare Company Needs Label Design

We need a label design for the first product of a new company called 'Vela'. We make skincare products made from natural ingredients.
Our initial product is a rose hip oil, and we need a label for the small 30mL bottle that it comes in, as well as for the box that the bottle will be sold in. The label will be printed directly onto the bottle, like the example in the attached photo. For reference, we like the look and feel of the labels on the bottle and box in the attached photos. It should convey a sense of natural.
The bottle will be dark green glass. For the name 'Vela' we like something close to orange so that it stands out. The rest of the text on the front of the bottle and box should read 'natural skincare' 'pure & organic' 'Rose hip oil' 'huile de cynorrhodon' 'pure et biologique'. '30mL' '1fl.oz'
We also like the silhouette of the main ingredient like in the attached photo. So a silhouette of a rose hip on the front of the bottle and box would be preferred.
On the right side of the bottle and box:
'Rose hip oil'
'Ingredients: 100% natural, cold pressed, Rosa canina (rose hip) seed oil'
'Benefits: Hydrates and refreshes skin, leaving a more even skin tone and a healthy glow'
'Application: Massage 3-4 drops into clean, damp skin twice daily or as required'
'Suitable for all skin types'
'Store below 30C'
On the left side of the bottle and box:
'Huile de Cynorrhodon'
'Ingredients/Constituants: huile de Rosa canina (cynorrhodon) 100% naturel, presse a froid'
'Bienfaits: rafraichit la peau, teint eblouissant'
'Mode d'emploi: Massez 3 a 4 gouttes sur une peau propre et humide deluxe fois par jour'
'Convient a tous les types de peau'
'Conserver a moins de 30C'

```html
<!DOCTYPE html>
<html lang="en">
<head>
<meta charset="utf-8">
<title>Vela Rose Hip Oil – Box and Bottle Label</title>
<link rel="stylesheet" href="https://fonts.googleapis.com/css2?family=Noticia+Text:ital,wght@0,400;0,700;1,400&display=swap">
<style>
  :root {
    --leaf-green: #5e874b;
    --stripe-orange: #f5a21f;
    --brand-orange: #f6a01e;
    --paper: #ffffff;
    --cap-dark: #2c2d2c;
    --glass-light: #62c97c;
    --glass-deep: #3f9c63;
    --sprig-tone: #e4e6df;
    --band-tone: rgba(255, 255, 255, 0.22);
  }
  html, body {
    margin: 0;
    padding: 0;
    width: 1165px;
    height: 1200px;
    overflow: hidden;
    background: var(--paper);
  }
  .artboard {
    display: block;
    width: 1165px;
    height: 1200px;
    font-family: "Noticia Text", Georgia, serif;
  }
  .carton-panel { fill: var(--leaf-green); }
  .stripe { fill: var(--stripe-orange); }
  .vine-band { fill: var(--band-tone); }
  .seal-disc { fill: var(--brand-orange); stroke: var(--paper); stroke-width: 3; }
  .seal-ring { fill: none; stroke: var(--paper); stroke-width: 1.4; }
  .brand-name { fill: var(--paper); font-weight: 400; text-anchor: middle; letter-spacing: 1px; }
  .panel-title { fill: var(--paper); font-weight: 700; font-size: 14px; }
  .label-head { fill: var(--paper); font-weight: 700; font-size: 10.5px; }
  .copy { fill: var(--paper); font-size: 10.5px; }
  .front-title { fill: var(--paper); font-weight: 700; text-anchor: middle; }
  .front-sub { fill: var(--paper); font-style: italic; text-anchor: middle; }
  .pill { fill: var(--paper); }
  .pill-text { fill: var(--leaf-green); text-anchor: middle; letter-spacing: .3px; }
  .volume { fill: var(--paper); text-anchor: middle; }
  .sprig { fill: var(--sprig-tone); }
  .dropper-cap { fill: var(--cap-dark); }
  .bottle-body { fill: url(#glass); }
  .micro { fill: var(--paper); font-size: 5.4px; }
  .micro-b { fill: var(--paper); font-size: 5.4px; font-weight: 700; }
</style>
</head>
<body>
<svg class="artboard" viewBox="0 0 1024 1060" preserveAspectRatio="none" xmlns="http://www.w3.org/2000/svg">
  <defs>
    <linearGradient id="glass" x1="0" y1="0" x2="0" y2="1">
      <stop offset="0" stop-color="var(--glass-light)"/>
      <stop offset="1" stop-color="var(--glass-deep)"/>
    </linearGradient>
  </defs>

  <g class="carton">
    <!-- Top dust flaps with tapered cutouts -->
    <path class="carton-panel" d="M75 423 L75 405 L84 394 L84 286 Q84 270 100 270 L234 270 Q248 270 248 286 L248 300 L255 312 L255 423 Z"/>
    <path class="carton-panel" d="M548 423 L548 312 L555 300 L555 286 Q555 270 571 270 L703 270 Q717 270 717 286 L717 394 L722 405 L722 423 Z"/>

    <!-- Top tuck lid -->
    <path class="carton-panel" d="M259 423 L259 195 Q259 163 291 163 L510 163 Q542 163 542 195 L542 423 Z"/>
    <g class="lid-stripes">
      <rect class="stripe" x="259" y="243" width="19" height="180"/>
      <rect class="stripe" x="307" y="243" width="24" height="180"/>
      <rect class="stripe" x="361" y="243" width="24" height="180"/>
      <rect class="stripe" x="415" y="243" width="24" height="180"/>
      <rect class="stripe" x="469" y="243" width="24" height="180"/>
      <rect class="stripe" x="523" y="243" width="19" height="180"/>
    </g>

    <!-- Main body -->
    <rect class="carton-panel" x="8" y="423" width="1004" height="440"/>

    <!-- Bottom dust flaps with tapered cutouts -->
    <path class="carton-panel" d="M75 862 L75 878 L82 888 L82 986 Q82 1000 97 1000 L236 1000 Q250 1000 250 986 L250 880 L255 870 L255 862 Z"/>
    <path class="carton-panel" d="M548 862 L548 870 L553 880 L553 986 Q553 1000 568 1000 L703 1000 Q717 1000 717 986 L717 888 L722 878 L722 862 Z"/>

    <!-- Bottom tuck flap -->
    <path class="carton-panel" d="M259 862 L542 862 L542 1028 Q542 1040 530 1040 L271 1040 Q259 1040 259 1028 Z"/>
    <g class="base-stripes">
      <rect class="stripe" x="259" y="862" width="19" height="172"/>
      <rect class="stripe" x="307" y="862" width="24" height="178"/>
      <rect class="stripe" x="361" y="862" width="24" height="178"/>
      <rect class="stripe" x="415" y="862" width="24" height="178"/>
      <rect class="stripe" x="469" y="862" width="24" height="178"/>
      <rect class="stripe" x="523" y="862" width="19" height="172"/>
    </g>

    <!-- Glue flap -->
    <path class="carton-panel" d="M728 862 L1012 862 L1012 1028 Q1012 1040 1000 1040 L740 1040 Q728 1040 728 1028 Z"/>
    <g class="glue-stripes">
      <rect class="stripe" x="728" y="862" width="22" height="172"/>
      <rect class="stripe" x="777" y="862" width="24" height="178"/>
      <rect class="stripe" x="831" y="862" width="24" height="178"/>
      <rect class="stripe" x="885" y="862" width="24" height="178"/>
      <rect class="stripe" x="939" y="862" width="24" height="178"/>
      <rect class="stripe" x="993" y="862" width="19" height="172"/>
    </g>

    <rect class="vine-band" x="40" y="486" width="970" height="14" role="img" aria-label="Twisting vine line ornament across the box"/>

    <!-- Front panel -->
    <g class="front-panel">
      <circle class="seal-disc" cx="402" cy="494" r="58"/>
      <text class="brand-name" x="402" y="505" font-size="30">Vela</text>
      <text class="front-title" x="402" y="593" font-size="15">Rose Hip Oil</text>
      <text class="front-sub" x="402" y="610" font-size="12.5">Huile de Cynorrhodon</text>
      <rect class="sprig" x="383" y="626" width="40" height="80" rx="10" role="img" aria-label="Rose hip plant silhouette with leaves and berries"/>
      <text class="front-title" x="402" y="736" font-size="13.5">Pure &amp; Organic</text>
      <text class="front-sub" x="402" y="753" font-size="12.5">Pure et Biologique</text>
      <rect class="pill" x="322" y="773" width="152" height="22" rx="11"/>
      <text class="pill-text" x="398" y="788" font-size="11">NATURAL SKINCARE</text>
      <text class="volume" x="402" y="836" font-size="12">30mL / 1fl.oz</text>
    </g>

    <!-- French side panel -->
    <g class="side-panel-fr">
      <text class="panel-title" x="83" y="555">Huile de Cynorrhodon</text>
      <text class="label-head" x="83" y="580">Ingredients/Constituants:</text>
      <text class="copy" x="83" y="598">Huile de Rosa canina</text>
      <text class="copy" x="83" y="611">(cynorrhodon) 100% naturel,</text>
      <text class="copy" x="83" y="624">presse a froid</text>
      <text class="label-head" x="83" y="649">Bienfaits:</text>
      <text class="copy" x="83" y="666">Rafraichit la peau, teint</text>
      <text class="copy" x="83" y="679">eblouissant</text>
      <text class="label-head" x="83" y="704">Mode d'emploi:</text>
      <text class="copy" x="83" y="721">Massez 3 a 4 gouttes sur une peau</text>
      <text class="copy" x="83" y="734">propre et humide deluxe fois par</text>
      <text class="copy" x="83" y="747">jour</text>
      <text class="copy" x="83" y="773">Convient a tous les types de peau</text>
      <text class="copy" x="83" y="798">Conserver a moins de 30°C</text>
    </g>

    <!-- English side panel -->
    <g class="side-panel-en">
      <text class="panel-title" x="551" y="555">Rose Hip Oil</text>
      <text class="label-head" x="551" y="580">Ingredients:</text>
      <text class="copy" x="551" y="598">100% natural, cold pressed, Rosa</text>
      <text class="copy" x="551" y="611">canina (rose hip) seed oil</text>
      <text class="label-head" x="551" y="636">Benefits:</text>
      <text class="copy" x="551" y="653">Hydrates and refreshes skin,</text>
      <text class="copy" x="551" y="666">leaving a more even skin tone and</text>
      <text class="copy" x="551" y="679">a healthy glow</text>
      <text class="label-head" x="551" y="704">Application:</text>
      <text class="copy" x="551" y="721">Massage 3-4 drops into clean,</text>
      <text class="copy" x="551" y="734">damp skin twice daily or as</text>
      <text class="copy" x="551" y="747">required</text>
      <text class="copy" x="551" y="773">Suitable for all skin types</text>
      <text class="copy" x="551" y="798">Store below 30°C</text>
    </g>

    <!-- Back panel -->
    <g class="back-panel">
      <circle class="seal-ring" cx="862" cy="604" r="34"/>
      <text class="brand-name" x="862" y="611" font-size="18">Vela</text>
      <rect class="sprig" x="832" y="655" width="68" height="128" rx="16" role="img" aria-label="Rose hip plant silhouette with leaves and berries"/>
    </g>
  </g>

  <!-- Bottle front -->
  <g class="bottle bottle-front">
    <path class="dropper-cap" d="M768 60 Q768 35 781 35 Q795 35 795 60 L795 100 L806 100 Q810 100 810 106 L810 188 L752 188 L752 106 Q752 100 758 100 L768 100 Z"/>
    <rect class="bottle-body" x="741" y="185" width="114" height="210" rx="18"/>
    <rect class="vine-band" x="743" y="214" width="110" height="6" role="img" aria-label="Twisting vine line ornament"/>
    <circle class="seal-disc" cx="798" cy="220" r="20" style="stroke-width:1.5"/>
    <text class="brand-name" x="798" y="225" font-size="12">Vela</text>
    <text class="front-title" x="798" y="266" font-size="10.5">Rose Hip Oil</text>
    <text class="front-sub" x="798" y="278" font-size="8.5">Huile de Cynorrhodon</text>
    <rect class="sprig" x="789" y="284" width="18" height="36" rx="5" role="img" aria-label="Rose hip plant silhouette"/>
    <text class="front-title" x="798" y="336" font-size="9">Pure &amp; Organic</text>
    <text class="front-sub" x="798" y="348" font-size="8.5">Pure et Biologique</text>
    <rect class="pill" x="759" y="359" width="78" height="10" rx="5"/>
    <text class="pill-text" x="798" y="367" font-size="6.2" style="fill:var(--glass-deep)">NATURAL SKINCARE</text>
    <text class="volume" x="798" y="381" font-size="7.5">30mL / 1fl.oz</text>
  </g>

  <!-- Bottle back -->
  <g class="bottle bottle-back">
    <path class="dropper-cap" d="M912 60 Q912 35 925 35 Q939 35 939 60 L939 100 L950 100 Q955 100 955 106 L955 188 L897 188 L897 106 Q897 100 903 100 L912 100 Z"/>
    <rect class="bottle-body" x="885" y="185" width="114" height="210" rx="18"/>
    <text x="891" y="234"><tspan class="micro-b">Rose Hip Oil - Ingredients:</tspan><tspan class="micro"> 100%</tspan></text>
    <text class="micro" x="891" y="241">natural, cold pressed, Rosa canina</text>
    <text class="micro" x="891" y="248">(rose hip) seed oil.</text>
    <text x="891" y="255"><tspan class="micro-b">Benefits:</tspan><tspan class="micro"> Hydrates and refreshes</tspan></text>
    <text class="micro" x="891" y="262">skin, leaving a more even skin tone</text>
    <text class="micro" x="891" y="269">and a healthy glow.</text>
    <text x="891" y="276"><tspan class="micro-b">Application:</tspan><tspan class="micro"> Massage 3-4 drops into</tspan></text>
    <text class="micro" x="891" y="283">clean, damp skin twice daily or as</text>
    <text class="micro" x="891" y="290">required. Suitable for all skin types.</text>
    <text class="micro" x="891" y="297">Store below 30°C</text>
    <text class="micro-b" x="891" y="314">Huile de Cynorrhodon-</text>
    <text class="micro-b" x="891" y="321">Ingredients/Constituants:</text>
    <text class="micro" x="891" y="328">Huile de Rosa canina (cynorrhodon)</text>
    <text class="micro" x="891" y="335">100% naturel, presse a froid.</text>
    <text x="891" y="342"><tspan class="micro-b">Bienfaits:</tspan><tspan class="micro"> Rafraichit la peau, teint</tspan></text>
    <text class="micro" x="891" y="349">eblouissant.</text>
    <text x="891" y="356"><tspan class="micro-b">Mode d'emploi:</tspan><tspan class="micro"> Massez 3 a 4 gouttes</tspan></text>
    <text class="micro" x="891" y="363">sur une peau propre et humide</text>
    <text class="micro" x="891" y="370">deluxe fois par jour.</text>
    <text class="micro" x="891" y="377">Convient a tous les types de peau</text>
    <text class="micro" x="891" y="384">Conserver a moins de 30°C</text>
  </g>
</svg>
</body>
</html>
```